I need a book cover for a 6x9 book. The front cover information (title and author) is below, and the back cover information will be given to the winning designer. I am wanting something vibrant and bright, and I am open to your creativity, but I do not want any pictures of people on the cover. Save room for the barcode on the back cover.
Title:
Oops! Wrong Turn?
Quiet Rooms Explained: Notes on Patient Gardening Habits
Author:
Marisol Tembe

```html
<!DOCTYPE html>
<html lang="en">
<head>
<meta charset="utf-8">
<title>Oops! Wrong Turn? — Book Cover</title>
<link rel="stylesheet" href="https://fonts.googleapis.com/css2?family=Bebas+Neue&family=Montserrat:wght@500;600&display=swap">
<style>
  :root {
    --page-bg: #ffffff;
    --cover-red-light: #f61c1c;
    --cover-red-mid: #e21116;
    --cover-red-dark: #cc0810;
    --title-yellow: #ffff00;
    --text-white: #ffffff;
  }
  html, body {
    margin: 0;
    padding: 0;
    width: 1200px;
    height: 1200px;
    overflow: hidden;
    background: var(--page-bg);
  }
  .canvas {
    position: relative;
    width: 1200px;
    height: 1200px;
  }
  .cover {
    position: absolute;
    left: 221px;
    top: 32px;
    width: 762px;
    height: 1143px;
    background: radial-gradient(ellipse at 50% 62%, var(--cover-red-light) 0%, var(--cover-red-mid) 45%, var(--cover-red-dark) 100%);
  }
  .cover-art {
    position: absolute;
    left: 0;
    top: 0;
    width: 1200px;
    height: 1200px;
  }
  .title-line {
    font-family: "Bebas Neue", "Oswald", sans-serif;
  }
  .title-line--accent { fill: var(--title-yellow); }
  .title-line--main { fill: var(--text-white); }
  .subtitle {
    position: absolute;
    left: 221px;
    width: 762px;
    top: 905px;
    margin: 0;
    text-align: center;
    font-family: "Montserrat", sans-serif;
    font-weight: 500;
    font-size: 31px;
    line-height: 49px;
  }
  .subtitle__lead { display: block; color: var(--text-white); }
  .subtitle__tail { display: block; color: var(--title-yellow); }
  .author {
    position: absolute;
    left: 221px;
    width: 762px;
    top: 1050px;
    margin: 0;
    text-align: center;
    font-family: "Montserrat", sans-serif;
    font-weight: 500;
    font-size: 52px;
    line-height: 64px;
    color: var(--text-white);
  }
</style>
</head>
<body>
<div class="canvas">
  <div class="cover"></div>

  <svg class="cover-art" viewBox="0 0 1200 1200" aria-labelledby="book-title">
    <title id="book-title">Oops! Wrong Turn?</title>
    <path class="speech-bubble"
          d="M346 91 H860 A51 51 0 0 1 911 142 V788 A51 51 0 0 1 860 839 H637 L594 876 Q583 884 583 872 V839 H346 A51 51 0 0 1 295 788 V142 A51 51 0 0 1 346 91 Z"
          fill="none" stroke="#ffffff" stroke-width="3.5" stroke-linejoin="round"/>
    <text class="title-line title-line--accent" x="339" y="315" font-size="257" textLength="529" lengthAdjust="spacingAndGlyphs">OOPS!</text>
    <text class="title-line title-line--main" x="339" y="606" font-size="391" textLength="525" lengthAdjust="spacingAndGlyphs">WRONG</text>
    <text class="title-line title-line--main" x="354" y="796" font-size="248" textLength="485" lengthAdjust="spacingAndGlyphs">TURN?</text>
  </svg>

  <p class="subtitle">
    <span class="subtitle__lead">Quiet Rooms Explained:</span>
    <span class="subtitle__tail">Notes on Patient Gardening Habits</span>
  </p>

  <p class="author">Marisol Tembe</p>
</div>
</body>
</html>
```